Flyer for Daycare

A Flyer for family group daycare
Specfs:
- One side english / Another Side spanish(the text for both sides is below)
- The flyer is for printing in 5" x 7" or 5.5" x 8.5"
- The address and phone number is the most important
Logo(see the attachment)
NYC Licensed
Children from 6 Weeks to 12 years old
Accepting All the Programs( TPB, OMW) and Private
CPR & First Aid Certified
Full Time, Part Time and After School
----------------------------------------------------------------------------
Provide Homework Assistance
Potty Training
Outdoor Activities
Nutritional Meals & Snack
Baby Wipes
Text in Spanish
Licencia por el estado de NY
Niños de 6 semanas a 12 años
Aceptando Todos los Programas (TPB, OMW) y Privado
Certificación en CPR y Primeros Auxilios
Tiempo completo, tiempo parcial y después de la escuela
----------------------------------------------------------------------------------------------
Actividades al aire libre
Asistencia con la tarea
Entrenamiento para ir al baño
Desayunos, Comidas y refrigerios nutricionales
Toallitas para bebé
582 E 416th ST
APT 4C
Bronx, NY, 10587
ig: @lumokidcare
555-718-2043
Target Market(s)
LAtin and Black, Bronx NY Area
Industry/Entity Type
Daycare service
Look and feel

```html
<!DOCTYPE html>
<html lang="en">
<head>
<meta charset="utf-8">
<title>Lumo Kid Care – Daycare Flyer</title>
<link rel="stylesheet" href="https://fonts.googleapis.com/css2?family=Lilita+One&family=Poppins:wght@500;600;700&display=swap">
<style>
  :root {
    --navy: #0b2a9c;
    --ink: #13237a;
    --sky: #6fd3f5;
    --sky-pale: #b9ecfb;
    --white: #ffffff;
    --purple: #a010b5;
    --purple-dark: #7a0a8c;
    --red: #e8141c;
    --green: #2aa012;
    --orange: #f39a13;
    --yellow: #ffd21f;
    --page: #e8e8e8;
  }
  * { margin: 0; padding: 0; box-sizing: border-box; }
  html, body { width: 734px; height: 1200px; overflow: hidden; }
  body { background: var(--page); font-family: "Poppins", sans-serif; position: relative; }

  .flyer {
    position: absolute; left: 17px; top: 110px;
    width: 700px; height: 980px; overflow: hidden;
    background: var(--sky);
    box-shadow: 0 6px 18px rgba(0,0,0,.18);
  }
  .flyer-backdrop { position: absolute; inset: 0; }

  .brand {
    position: absolute; left: 40px; top: 110px;
    display: flex; align-items: center; gap: 12px;
  }
  .brand-dot { width: 34px; height: 34px; border-radius: 50%; background: var(--purple); }
  .brand-name { font-weight: 700; font-size: 34px; color: var(--purple); letter-spacing: .5px; }

  .headline {
    position: absolute; left: 42px; top: 262px;
    font-family: "Lilita One", sans-serif; font-size: 82px; line-height: 1;
    color: var(--navy); letter-spacing: 1px;
  }
  .licensed {
    position: absolute; left: 45px; top: 344px;
    width: 170px; height: 44px; border-radius: 22px 8px 22px 8px;
    background: var(--red); color: var(--white);
    font-family: "Lilita One", sans-serif; font-size: 22px;
    display: flex; align-items: center; justify-content: center;
    box-shadow: 3px 4px 0 #555;
  }
  .ages { position: absolute; left: 226px; top: 340px; line-height: 1.1; }
  .ages-lead { font-size: 19px; font-weight: 500; color: #222; }
  .ages-range { font-family: "Lilita One", sans-serif; font-size: 24px; }
  .ages-range .weeks { color: var(--green); }
  .ages-range .years { color: var(--orange); }
  .ages-range small { font-size: 16px; }

  .photo {
    position: absolute;
  }
  .photo-wall {
    left: 414px; top: 160px; width: 290px; height: 330px;
    border-radius: 140px 0 0 140px;
    background: linear-gradient(160deg, #f4f4f4, #dcdcdc 55%, #f0c8d0);
  }
  .photo-kids {
    left: 0; top: 620px; width: 400px; height: 360px;
    background: linear-gradient(180deg, #9fdcf2 0%, #e9c6a8 45%, #8fa9c9 75%, #f2a13a 100%);
    -webkit-mask: linear-gradient(180deg, transparent 0, #000 18%);
            mask: linear-gradient(180deg, transparent 0, #000 18%);
  }

  .feature {
    position: absolute; width: 166px; height: 166px; border-radius: 50%;
    background: var(--purple); border: 4px solid var(--purple-dark);
    box-shadow: -4px 4px 0 rgba(80,0,90,.35);
    color: var(--white); text-align: center;
    display: flex; flex-direction: column; align-items: center; justify-content: center;
    font-weight: 600; font-size: 17px; line-height: 1.15;
  }
  .feature svg { margin-bottom: 6px; }
  .feature small { font-size: 8px; display: block; }
  .feature-programs { left: 55px; top: 432px; }
  .feature-cpr { left: 271px; top: 432px; }
  .feature-hours { left: 478px; top: 432px; }

  .provide { position: absolute; left: 367px; top: 606px; }
  .provide h2 { font-family: "Lilita One", sans-serif; font-weight: 400; font-size: 34px; color: var(--navy); line-height: 1.1; margin-bottom: 4px; }
  .provide ul { list-style: none; }
  .provide li { font-size: 17px; font-weight: 600; color: var(--ink); height: 28px; display: flex; align-items: center; gap: 4px; }

  .contact { position: absolute; right: 46px; top: 848px; text-align: right; color: var(--ink); }
  .contact-phone { font-family: "Lilita One", sans-serif; font-size: 30px; display: flex; align-items: center; justify-content: flex-end; gap: 4px; line-height: 1.1; }
  .contact-social { font-family: "Lilita One", sans-serif; font-size: 23px; display: flex; align-items: center; justify-content: flex-end; gap: 6px; margin-top: 4px; }
  .social-dot { width: 16px; height: 16px; border-radius: 4px; border: 2.5px solid var(--purple); }
  .contact-address { font-size: 12.5px; font-weight: 600; display: flex; align-items: center; justify-content: flex-end; gap: 3px; margin-top: 6px; }
</style>
</head>
<body>
<main class="flyer">
  <svg class="flyer-backdrop" viewBox="0 0 700 980" width="700" height="980" aria-hidden="true">
    <defs>
      <linearGradient id="skyFade" x1="0" y1="0" x2="0" y2="1">
        <stop offset="0" stop-color="#8fdcf7"/>
        <stop offset="1" stop-color="#52c6f2"/>
      </linearGradient>
    </defs>
    <rect width="700" height="980" fill="url(#skyFade)"/>
    <rect width="700" height="250" fill="var(--navy)"/>
    <path d="M0 170 C40 150 70 120 110 130 C130 80 200 60 250 80 C290 30 370 40 390 90 C440 70 500 80 520 120 C570 100 640 120 660 160 C690 150 700 170 700 180 L700 470 C640 480 560 470 520 480 C440 470 380 420 300 440 C200 420 100 420 0 390 Z" fill="var(--white)"/>
    <path d="M380 820 C420 790 470 800 490 815 C520 780 600 780 620 810 C650 790 690 800 700 810 L700 980 L380 980 Z" fill="var(--white)"/>
  </svg>

  <div class="brand"><span class="brand-dot"></span><span class="brand-name">Lumo Kid Care</span></div>

  <h1 class="headline">DAYCARE</h1>
  <div class="licensed">NYC LICENSED</div>
  <div class="ages">
    <div class="ages-lead">Children from</div>
    <div class="ages-range"><span class="weeks">6 <small>WEEKS</small></span> - <span class="years">12 <small>YEARS</small></span></div>
  </div>

  <div class="photo photo-wall" role="img" aria-label="Photo of two children with backpacks drawing on a white wall with large pencils"></div>

  <div class="feature feature-programs">
    <svg width="30" height="24" viewBox="0 0 30 24" aria-hidden="true"><path d="M2 3h10c2 0 3 1 3 3v16c0-1-1-2-3-2H2Z M28 3H18c-2 0-3 1-3 3v16c0-1 1-2 3-2h10Z" fill="var(--yellow)"/></svg>
    <span>Accepting All<br>the Programs</span>
    <small>( TPB, OMW)</small>
    <span>and Private</span>
  </div>
  <div class="feature feature-cpr">
    <svg width="32" height="26" viewBox="0 0 32 26" aria-hidden="true"><rect x="11" y="1" width="10" height="5" rx="1.5" fill="none" stroke="var(--yellow)" stroke-width="2.5"/><rect x="2" y="5" width="28" height="20" rx="3" fill="var(--yellow)"/><circle cx="16" cy="15" r="6" fill="var(--purple)"/><path d="M16 11v8M12 15h8" stroke="var(--yellow)" stroke-width="2.5"/></svg>
    <span>CPR &amp; First<br>Aid Certified</span>
  </div>
  <div class="feature feature-hours">
    <svg width="32" height="30" viewBox="0 0 32 30" aria-hidden="true"><path d="M16 2l7 7v3h7v17H2V12h7V9Z" fill="var(--yellow)"/><circle cx="16" cy="10" r="2.5" fill="var(--purple)"/><rect x="13" y="19" width="6" height="10" fill="var(--purple)"/><rect x="5" y="16" width="4" height="4" fill="var(--purple)"/><rect x="23" y="16" width="4" height="4" fill="var(--purple)"/></svg>
    <span>Full Time, Part<br>Time and After<br>School</span>
  </div>

  <div class="photo photo-kids" role="img" aria-label="Photo of two smiling children looking through colourful toy rings at a table with toys"></div>

  <section class="provide">
    <h2>We provide</h2>
    <ul>
      <li><svg width="20" height="18" viewBox="0 0 20 18" aria-hidden="true"><path d="M2 10l5 5L18 2" fill="none" stroke="var(--purple)" stroke-width="3.5" stroke-linecap="round"/></svg>Provide Homework Assistance</li>
      <li><svg width="20" height="18" viewBox="0 0 20 18" aria-hidden="true"><path d="M2 10l5 5L18 2" fill="none" stroke="var(--purple)" stroke-width="3.5" stroke-linecap="round"/></svg>Potty Training</li>
      <li><svg width="20" height="18" viewBox="0 0 20 18" aria-hidden="true"><path d="M2 10l5 5L18 2" fill="none" stroke="var(--purple)" stroke-width="3.5" stroke-linecap="round"/></svg>Outdoor Activities</li>
      <li><svg width="20" height="18" viewBox="0 0 20 18" aria-hidden="true"><path d="M2 10l5 5L18 2" fill="none" stroke="var(--purple)" stroke-width="3.5" stroke-linecap="round"/></svg>Nutritional Meals &amp; Snack</li>
      <li><svg width="20" height="18" viewBox="0 0 20 18" aria-hidden="true"><path d="M2 10l5 5L18 2" fill="none" stroke="var(--purple)" stroke-width="3.5" stroke-linecap="round"/></svg>Baby Wipes</li>
    </ul>
  </section>

  <address class="contact" style="font-style:normal">
    <div class="contact-phone"><svg width="22" height="22" viewBox="0 0 24 24" aria-hidden="true"><path d="M6.6 10.8a15 15 0 006.6 6.6l2.2-2.2c.3-.3.7-.4 1-.2 1.1.4 2.3.6 3.6.6.6 0 1 .4 1 1V20c0 .6-.4 1-1 1A17 17 0 013 4c0-.6.4-1 1-1h3.5c.6 0 1 .4 1 1 0 1.3.2 2.5.6 3.6.1.3 0 .7-.2 1Z" fill="var(--orange)"/></svg>555-718-2043</div>
    <div class="contact-social"><span class="social-dot"></span>@lumokidcare</div>
    <div class="contact-address"><svg width="12" height="16" viewBox="0 0 12 16" aria-hidden="true"><path d="M6 0a6 6 0 00-6 6c0 4.5 6 10 6 10s6-5.5 6-10a6 6 0 00-6-6Zm0 8.3A2.3 2.3 0 116 3.7a2.3 2.3 0 010 4.6Z" fill="var(--red)"/></svg>582 E 416th ST APT 4C Bronx, NY, 10587</div>
  </address>
</main>
</body>
</html>
```